Brightvolt Electrical Services Needs A Flyer Design

We need a flyer design for a new business based in Sydney, Australia called Brightvolt Electrical Services. We provide services for residential,commercial and industrial works. Services include Electrical Design, Installation, Repairs & Maintenance. Communications Installation, Cabling, Maintenance & Repairs. Over 25 years Industry Experience.Service Calls, Quick Response Time, Professional Service. We would like to see designs that use the colors red,white and blue similar to the logo. The final Design should be creative as the business logo suggests and should communicate the businesses services.

Target Market(s)

Residential

Industry/Entity Type

Industrial

Font styles to use
Sans Serif

Requirements
Must have
• My project must have the logo provided utilized in the flyer.It must list the following contact name and number Ray 0491 627 318 services as above in the project description. Flyer should be DL size (99mmx210mm).

```html
<!DOCTYPE html>
<html lang="en">
<head>
<meta charset="utf-8">
<title>Brightvolt Electrical Services – DL Flyer</title>
<link rel="stylesheet" href="https://fonts.googleapis.com/css2?family=Montserrat:wght@800&family=Oswald:wght@300;400;500&family=Roboto+Condensed:wght@400;700&display=swap">
<style>
  :root {
    --navy: #141c45;
    --navy-deep: #0e1434;
    --red: #d7262c;
    --red-dark: #b81c22;
    --white: #ffffff;
    --ink: #1a1f3f;
    --rule-blue: #2b3a8c;
    --bg: #e9ebef;
    --wire-copper: #c8432a;
    --wire-blue: #3a3f9a;
  }
  * { margin: 0; padding: 0; box-sizing: border-box; }
  html, body { width: 1200px; height: 800px; overflow: hidden; }
  body { background: var(--bg); position: relative; font-family: "Roboto Condensed", Arial, sans-serif; }

  .flyer {
    position: absolute;
    top: 50px;
    width: 330px;
    height: 700px;
    background: var(--white);
    overflow: hidden;
    box-shadow: 0 6px 20px rgba(0,0,0,.18);
  }
  .flyer--front { left: 225px; }
  .flyer--back { left: 645px; border: 6px solid var(--red); }

  .shape { position: absolute; left: 0; width: 100%; display: block; }

  /* Brand name */
  .brand {
    position: absolute;
    font-family: "Montserrat", Arial, sans-serif;
    font-weight: 800;
    color: var(--navy);
    line-height: 1;
    text-align: center;
  }
  .brand__name { display: block; letter-spacing: 1px; }
  .brand__sub { display: block; letter-spacing: 2px; }

  .flyer--front .brand { left: 0; right: 0; top: 220px; }
  .flyer--front .brand__name { font-size: 38px; }
  .flyer--front .brand__sub { font-size: 12.5px; margin-top: 8px; }

  /* Front lower panel */
  .experience {
    position: absolute;
    left: 0; right: 0; top: 480px;
    text-align: center;
    color: #c9cdf0;
    font-family: "Montserrat", Arial, sans-serif;
    font-weight: 800;
    line-height: .95;
  }
  .experience__num { display: block; font-size: 78px; color: #dde0ff; }
  .experience__years { display: block; font-size: 30px; }
  .experience__label { display: block; font-size: 17px; margin-top: 2px; }

  .wire-art {
    position: absolute;
    left: 0; right: 0;
    height: 46px;
    background: linear-gradient(90deg, var(--wire-copper) 0%, #e0704d 38%, #e9f0ff 50%, #6d72c7 62%, var(--wire-blue) 100%);
    opacity: .8;
  }
  .flyer--front .wire-art { top: 528px; height: 30px; }
  .flyer--back .wire-art { top: 355px; }

  /* Back top */
  .flyer--back .brand { left: 14px; right: 14px; top: 26px; }
  .flyer--back .brand__name { font-size: 34px; }
  .flyer--back .brand__sub { font-size: 11px; margin-top: 7px; }

  .bulb-art {
    position: absolute;
    left: 14px; top: 100px;
    width: 120px; height: 230px;
    background: radial-gradient(ellipse at 50% 40%, #eef1fb 0%, #dfe4f5 60%, #ffffff 100%);
    border-radius: 60px 60px 14px 14px;
  }

  .intro {
    position: absolute;
    left: 140px; right: 10px; top: 108px;
    text-align: center;
    color: var(--ink);
  }
  .intro__lead { font-size: 14px; }
  .intro__sectors { font-size: 14px; font-weight: 700; line-height: 1.2; }

  .highlights {
    position: absolute;
    left: 130px; right: 10px; top: 168px;
    list-style: none;
    text-align: center;
    color: var(--red);
    font-family: "Oswald", Arial, sans-serif;
    font-weight: 300;
    font-size: 21px;
    line-height: 1.18;
  }

  .values {
    position: absolute;
    left: 130px; right: 12px; top: 262px;
    border-top: 1.5px solid var(--rule-blue);
    border-bottom: 1.5px solid var(--rule-blue);
    padding: 6px 0;
    text-align: center;
    font-weight: 700;
    font-size: 15px;
    color: var(--ink);
  }

  .service-list {
    position: absolute;
    left: 92px; top: 430px;
    list-style: none;
    color: var(--white);
    font-family: "Oswald", Arial, sans-serif;
    font-weight: 300;
    font-size: 13.5px;
    letter-spacing: .4px;
  }
  .service-list li { display: flex; align-items: center; gap: 8px; height: 23px; }
  .pin { width: 10px; height: 13px; flex: none; }

  .call-out {
    position: absolute;
    left: 0; right: 0; top: 590px;
    text-align: center;
    color: var(--white);
    font-family: "Oswald", Arial, sans-serif;
    font-weight: 400;
    font-size: 16px;
    letter-spacing: .6px;
  }

  .contact-band {
    position: absolute;
    left: 0; right: 0; bottom: 0;
    height: 62px;
    background: var(--red);
    display: flex; align-items: center; justify-content: center; gap: 8px;
    color: var(--white);
    font-family: "Oswald", Arial, sans-serif;
    font-size: 28px;
    letter-spacing: .5px;
  }
  .contact-band__name { font-weight: 500; }
  .contact-band__phone { font-weight: 300; }
</style>
</head>
<body>

  <!-- Front of flyer -->
  <section class="flyer flyer--front" aria-label="Flyer front">
    <svg class="shape" style="top:0;height:90px" viewBox="0 0 330 90" preserveAspectRatio="none" aria-hidden="true">
      <polygon points="0,0 330,0 330,52 210,52 228,78 90,66 70,80 0,74" fill="var(--red)"/>
      <polygon points="0,0 330,0 330,30 0,44" fill="var(--red-dark)"/>
    </svg>

    <div class="brand">
      <span class="brand__name">BRIGHTVOLT</span>
      <span class="brand__sub">ELECTRICAL SERVICES</span>
    </div>

    <svg class="shape" style="top:340px;height:360px" viewBox="0 0 330 360" preserveAspectRatio="none" aria-hidden="true">
      <polygon points="0,10 200,22 184,34 330,40 330,360 0,360" fill="var(--navy)"/>
      <polyline points="0,20 190,30 176,42 330,48" fill="none" stroke="var(--white)" stroke-width="3"/>
    </svg>

    <div class="wire-art" role="img" aria-label="Illustration of two electrical wires meeting with sparks"></div>

    <div class="experience">
      <span class="experience__num">25</span>
      <span class="experience__years">Years</span>
      <span class="experience__label">Experience</span>
    </div>
  </section>

  <!-- Back of flyer -->
  <section class="flyer flyer--back" aria-label="Flyer back">
    <div class="brand">
      <span class="brand__name">BRIGHTVOLT</span>
      <span class="brand__sub">ELECTRICAL SERVICES</span>
    </div>

    <div class="bulb-art" role="img" aria-label="Line drawing of a light bulb"></div>

    <div class="intro">
      <p class="intro__lead">Services for</p>
      <p class="intro__sectors">Residential, Commercial and Industrial Works</p>
    </div>

    <ul class="highlights">
      <li>Service Calls</li>
      <li>Quick Response Time</li>
      <li>Professional Service</li>
    </ul>

    <p class="values">Clean, Trustworthy, Affordable</p>

    <svg class="shape" style="top:336px;height:364px" viewBox="0 0 318 364" preserveAspectRatio="none" aria-hidden="true">
      <polygon points="0,10 318,4 318,364 0,364" fill="var(--navy)"/>
    </svg>

    <div class="wire-art" role="img" aria-label="Illustration of two electrical wires meeting with sparks"></div>

    <ul class="service-list">
      <li><svg class="pin" viewBox="0 0 10 13" aria-hidden="true"><path d="M5 0a5 5 0 0 1 5 5c0 3.5-5 8-5 8S0 8.5 0 5a5 5 0 0 1 5-5z" fill="var(--red)"/><circle cx="5" cy="5" r="1.8" fill="var(--white)"/></svg>ELECTRICAL DESIGN</li>
      <li><svg class="pin" viewBox="0 0 10 13" aria-hidden="true"><path d="M5 0a5 5 0 0 1 5 5c0 3.5-5 8-5 8S0 8.5 0 5a5 5 0 0 1 5-5z" fill="var(--red)"/><circle cx="5" cy="5" r="1.8" fill="var(--white)"/></svg>INSTALLATION</li>
      <li><svg class="pin" viewBox="0 0 10 13" aria-hidden="true"><path d="M5 0a5 5 0 0 1 5 5c0 3.5-5 8-5 8S0 8.5 0 5a5 5 0 0 1 5-5z" fill="var(--red)"/><circle cx="5" cy="5" r="1.8" fill="var(--white)"/></svg>REPAIRS &amp; MAINTENANCE</li>
      <li><svg class="pin" viewBox="0 0 10 13" aria-hidden="true"><path d="M5 0a5 5 0 0 1 5 5c0 3.5-5 8-5 8S0 8.5 0 5a5 5 0 0 1 5-5z" fill="var(--red)"/><circle cx="5" cy="5" r="1.8" fill="var(--white)"/></svg>COMMUNICATIONS INSTALLATION</li>
      <li><svg class="pin" viewBox="0 0 10 13" aria-hidden="true"><path d="M5 0a5 5 0 0 1 5 5c0 3.5-5 8-5 8S0 8.5 0 5a5 5 0 0 1 5-5z" fill="var(--red)"/><circle cx="5" cy="5" r="1.8" fill="var(--white)"/></svg>CABLING</li>
      <li><svg class="pin" viewBox="0 0 10 13" aria-hidden="true"><path d="M5 0a5 5 0 0 1 5 5c0 3.5-5 8-5 8S0 8.5 0 5a5 5 0 0 1 5-5z" fill="var(--red)"/><circle cx="5" cy="5" r="1.8" fill="var(--white)"/></svg>MAINTENANCE &amp; REPAIRS</li>
    </ul>

    <p class="call-out">CALL TODAY FOR YOUR ELECTRICAL NEEDS</p>

    <div class="contact-band">
      <span class="contact-band__name">RAY</span>
      <span class="contact-band__phone">0491 627 318</span>
    </div>
  </section>

</body>
</html>
```